Birchwood Turf Care_2015 New Cards_V1

We need an enhanced business card from what we have today. We are a Landscaping company and we have an existing Logo and text info that we would like to include.
Text to include:
In business for over 20 years,Fully Insured, Weekly Lawn Maintenance, Spring & Fall Clean-up, Dale Whitford, 203-555-0147, www.birchwoodturfcarect.example, Visit our Website for additional Lawn Care Services or email directly at DALE@BIRCHWOODTURFCARE.EXAMPLE, We appreciate your business.
We want full color background and we will want to take this design and work with a printer that does high graphic silk screen cards. The colors we have thought about are Black, with our Green Logo, with Gold Text...we are open to different colors, we just want the card to wow!

Target Market(s)

Lawn Care Maintenance

Industry/Entity Type

Lawn Care

Contact Information for Business Card

Text to include:
In business for over 20 years, Fully Insured, Weekly Lawn Maintenance, Spring & Fall Clean-up, Dale Whitford, 203-555-0147, www.birchwoodturfcarect.example, Visit our Website for additional Lawn Care Services or email directly at DALE@BIRCHWOODTURFCARE.EXAMPLE, We appreciate your business.

Requirements
Must have
• Logo, text details about how to reach us, standard size business cards that go horizontal.
Nice to have
• background colors, background designs, raised embossed lettering, rounded corners(2 or 4),

```html
<!DOCTYPE html>
<html lang="en">
<head>
<meta charset="utf-8">
<title>Birchwood Turf Care – Business Cards</title>
<link rel="stylesheet" href="https://fonts.googleapis.com/css2?family=Source+Sans+3:wght@400;600;700&display=swap">
<style>
  :root {
    --backdrop: #4b403b;
    --card: #1c1c1d;
    --card-edge: #2a2a2b;
    --white: #f1f1f1;
    --muted: #8d8d8d;
    --orange: #ea5a22;
    --rule: #cfcfcf;
  }
  * { box-sizing: border-box; margin: 0; padding: 0; }
  html, body {
    width: 1200px; height: 865px; overflow: hidden;
    background: var(--backdrop);
    font-family: "Source Sans 3", Arial, sans-serif;
  }
  .canvas { position: relative; width: 1200px; height: 865px; }

  .card {
    position: absolute;
    width: 580px; height: 332px;
    background: var(--card);
    border: 1px solid var(--card-edge);
    border-radius: 6px;
    box-shadow: 0 10px 24px rgba(0,0,0,.45);
  }
  .card--back  { left: 50px;  top: 70px; }
  .card--front { left: 570px; top: 460px; }

  /* Wordmark */
  .wordmark { display: flex; align-items: center; gap: 14px; position: absolute; }
  .wordmark__dot { width: 22px; height: 22px; border-radius: 50%; background: var(--orange); flex: none; }
  .wordmark__name {
    font-weight: 700; font-size: 40px; letter-spacing: 2px;
    text-transform: uppercase; line-height: 1; white-space: nowrap;
  }
  .card--back .wordmark { left: 54px; top: 70px; }
  .card--back .wordmark__name { color: var(--muted); }
  .card--front .wordmark { right: 40px; top: 52px; }
  .card--front .wordmark__name { color: var(--white); font-size: 34px; }

  /* Back tagline */
  .tagline {
    position: absolute; left: 54px; top: 160px;
    color: var(--orange); font-size: 23px; line-height: 1.3;
  }
  .tagline span { display: block; }
  .tagline span + span { padding-left: 44px; }

  /* Front details */
  .details { position: absolute; left: 30px; right: 30px; top: 150px; display: flex; }
  .person { width: 262px; text-align: right; padding-right: 20px; border-right: 1px solid var(--rule); }
  .person__name { color: var(--orange); font-weight: 700; font-size: 25px; line-height: 1.05; text-transform: uppercase; }
  .person__role { color: var(--white); font-size: 18px; margin-bottom: 8px; }
  .person__service { color: var(--white); font-size: 18px; line-height: 1.3; }
  .contact { padding-left: 18px; list-style: none; display: flex; flex-direction: column; gap: 9px; padding-top: 14px; }
  .contact li { display: flex; align-items: center; gap: 9px; color: var(--white); font-size: 18px; white-space: nowrap; }
  .contact svg { width: 14px; height: 14px; flex: none; fill: var(--orange); }
</style>
</head>
<body>
<main class="canvas">

  <section class="card card--back" aria-label="Card back">
    <div class="wordmark">
      <span class="wordmark__dot"></span>
      <span class="wordmark__name">Birchwood Turf Care</span>
    </div>
    <p class="tagline">
      <span>In business for over 20 years</span>
      <span>Fully Insured</span>
    </p>
  </section>

  <section class="card card--front" aria-label="Card front">
    <div class="wordmark">
      <span class="wordmark__dot"></span>
      <span class="wordmark__name">Birchwood Turf Care</span>
    </div>
    <div class="details">
      <div class="person">
        <p class="person__name">Dale Whitford</p>
        <p class="person__role">Owner</p>
        <p class="person__service">Weekly Lawn Maintenance</p>
        <p class="person__service">Spring &amp; Fall Clean-Ups</p>
      </div>
      <ul class="contact">
        <li>
          <svg viewBox="0 0 16 16" aria-hidden="true"><path d="M3.5 1.5l2.5 0 1 3.5-1.6 1.2c.8 1.7 2.2 3.1 3.9 3.9l1.2-1.6 3.5 1v2.5c0 .8-.7 1.5-1.5 1.5C6.8 13.5 2 8.7 2 3c0-.8.7-1.5 1.5-1.5z"/></svg>
          (203) 555-0147
        </li>
        <li>
          <svg viewBox="0 0 16 16" aria-hidden="true"><path d="M1 3h14v10H1z M2 4.2v.5l6 4 6-4v-.5z" fill-rule="evenodd"/></svg>
          dale@birchwoodturfcare.example
        </li>
        <li>
          <svg viewBox="0 0 16 16" aria-hidden="true"><path d="M8 1a7 7 0 1 0 0 14A7 7 0 0 0 8 1zm0 1.4c.8.8 1.4 2.2 1.6 3.6H6.4C6.6 4.6 7.2 3.2 8 2.4zM2.5 7h2.8c0 .7 0 1.3.1 2H2.5a5.6 5.6 0 0 1 0-2zm4 0h3c0 .7 0 1.3-.1 2H6.6c-.1-.7-.1-1.3-.1-2zm4.2 0h2.8a5.6 5.6 0 0 1 0 2h-2.9c.1-.7.1-1.3.1-2zM6.4 10h3.2c-.2 1.4-.8 2.8-1.6 3.6-.8-.8-1.4-2.2-1.6-3.6z"/></svg>
          www.birchwoodturfcare.example
        </li>
        <li style="padding-left:23px">www.birchwoodturfcarect.example</li>
      </ul>
    </div>
  </section>

</main>
</body>
</html>
```